Building company with a modern and unique product looking for a business card to help us stand out

We currently have a logo but as our business has grown, we feel that our business card is not reflecting our modern and high quality product and help us stand out from the crowd. Our business is mainly in the construction of new homes using a unique method and materials that makes our homes fire proof, vermin and pest resistant and rated to the maximum cyclone category (category 5). We need a business card that helps us stand out as well as communicating professionalism, high quality and trustworthiness. I have attached our current logo with a black and white option, as well as our business card which is double sided. We would like to retain as much of the information that is currently on our business cards, but presented in a more sleek way. We do like our current colour palette ( white, black, yellow and grey) and have been looking primarily at business cards with a black background however we are open to other combinations of colour and layout as long as we stand out. Please feel free to tweak our logo to make it more suitable for a business card, we like the black option that we use but we have had trouble trying to get the white area to match the rest of the logo and blend effectively into a business card. Please do not hesitate to contact us with any questions as we really want this to be successful!

Target Market(s)

Large contracts including government and larger companies

Industry/Entity Type

Business

We will be providing this business card to potential clients including key government ministers and large funding companies, our business card should show that we are professional and reliable.

Requirements
Must have
• It must be easy to read and pleasing to the eye, It must contain as much of the information on the current business card and unless something really stands out, we will most likely pick a design that has all of the information included. It must include our logo of course and have some colour included.
Nice to have
• We are looking for a high end business card and would like to see designs that reflect this. We like the gloss/matte contrast, plastic cards with opaque/coloured areas and unique features not seen on everyday paper business cards. It would be nice to see a few different colour combinations, we are open to new ideas so please feel free to take some artistic licence.
Should not have
• Must not be too busy, difficult to read or be distracting from the information conveyed. Other than this please feel free to add your own touches and make it unique!

```html
<!DOCTYPE html>
<html lang="en">
<head>
<meta charset="utf-8">
<title>Norvale Building Company – Business Card</title>
<link rel="stylesheet" href="https://fonts.googleapis.com/css2?family=Open+Sans:wght@400;600;700&display=swap">
<style>
  :root {
    --canvas: #e4e4e4;
    --card-white: #ffffff;
    --card-dark: #3c3c3e;
    --ink: #1b1b1b;
    --ink-soft: #555555;
    --band: #1a1a1a;
    --accent: #f2e600;
    --pattern: #ececec;
    --text-on-dark: #f1f1f1;
  }
  * { box-sizing: border-box; margin: 0; padding: 0; }
  html, body {
    width: 1200px; height: 900px; overflow: hidden;
    background: var(--canvas);
    font-family: "Open Sans", Arial, sans-serif;
  }
  .canvas {
    width: 1200px; height: 900px;
    display: flex; flex-direction: column; align-items: center; justify-content: center;
    gap: 60px;
  }
  .card {
    position: relative;
    width: 560px; height: 320px;
    overflow: hidden;
    box-shadow: 0 6px 18px rgba(0,0,0,.18);
  }

  /* Front */
  .card-front { background: var(--card-white); }
  .front-pattern {
    position: absolute; inset: 0;
    background: linear-gradient(160deg, var(--card-white) 0%, var(--pattern) 45%, var(--card-white) 75%);
  }
  .front-brand {
    position: absolute; left: 34px; top: 118px;
    display: flex; align-items: center; gap: 10px;
  }
  .brand-mark { width: 16px; height: 16px; background: var(--accent); }
  .brand-name {
    font-size: 21px; font-weight: 700; color: var(--ink); line-height: 1.1;
  }
  .contact {
    position: absolute; left: 300px; top: 40px;
    color: var(--ink);
  }
  .contact-name { font-size: 17px; font-weight: 700; }
  .contact-role { font-size: 11px; color: var(--ink-soft); margin-bottom: 12px; }
  .contact-list { list-style: none; }
  .contact-item {
    display: flex; align-items: center; gap: 10px;
    font-size: 13px; margin-bottom: 6px;
  }
  .contact-icon { width: 14px; height: 14px; fill: var(--ink); flex: none; }

  .front-band { position: absolute; left: 0; bottom: 0; width: 560px; height: 120px; }
  .band-text {
    position: absolute; left: 0; right: 0; bottom: 16px;
    color: var(--text-on-dark); text-align: center;
  }
  .band-lead { font-size: 14px; margin-bottom: 6px; }
  .band-features {
    display: flex; justify-content: center; gap: 18px;
    list-style: none; font-size: 14px;
  }
  .feature { display: flex; align-items: center; gap: 6px; }
  .tick { width: 13px; height: 13px; flex: none; }

  /* Back */
  .card-back {
    background: radial-gradient(ellipse at 50% 45%, #58585a 0%, var(--card-dark) 55%);
    display: flex; align-items: center; justify-content: center;
  }
  .back-brand {
    display: flex; align-items: center; gap: 12px;
  }
  .back-brand .brand-mark { width: 18px; height: 18px; background: #141414; }
  .back-brand .brand-name { font-size: 28px; color: #141414; }
</style>
</head>
<body>
<main class="canvas">

  <section class="card card-front" aria-label="Business card front">
    <div class="front-pattern" role="img" aria-label="Faint grey angled roofline pattern"></div>

    <div class="front-brand">
      <span class="brand-mark"></span>
      <span class="brand-name">Norvale Building<br>Company</span>
    </div>

    <div class="contact">
      <p class="contact-name">Callum Reeves</p>
      <p class="contact-role">Managing Director</p>
      <ul class="contact-list">
        <li class="contact-item">
          <svg class="contact-icon" viewBox="0 0 16 16"><rect x="4" y="1" width="8" height="14" rx="1.5"/><rect x="5.5" y="3" width="5" height="8" fill="#fff"/></svg>
          : 0400 555 218
        </li>
        <li class="contact-item">
          <svg class="contact-icon" viewBox="0 0 16 16"><path d="M4 1l3 3-2 2c1 2 3 4 5 5l2-2 3 3-2 3C7 14 2 9 1 3z"/></svg>
          : (02) 5550 1734
        </li>
        <li class="contact-item">
          <svg class="contact-icon" viewBox="0 0 16 16"><rect x="1" y="3" width="14" height="10" rx="1"/><path d="M2 4l6 5 6-5" stroke="#fff" stroke-width="1.4" fill="none"/></svg>
          : hello@norvalebuild.com
        </li>
      </ul>
    </div>

    <svg class="front-band" viewBox="0 0 560 120" preserveAspectRatio="none">
      <path d="M0 44 Q280 30 560 0 L560 120 L0 120 Z" fill="var(--accent)"/>
      <path d="M0 52 Q280 38 560 10 L560 120 L0 120 Z" fill="var(--band)"/>
    </svg>
    <div class="band-text">
      <p class="band-lead">Specializing in Homes that are</p>
      <ul class="band-features">
        <li class="feature"><svg class="tick" viewBox="0 0 14 14"><rect width="14" height="14" fill="var(--accent)"/><path d="M3 7l3 3 5-6" stroke="#1a1a1a" stroke-width="2" fill="none"/></svg>Fire Proof</li>
        <li class="feature"><svg class="tick" viewBox="0 0 14 14"><rect width="14" height="14" fill="var(--accent)"/><path d="M3 7l3 3 5-6" stroke="#1a1a1a" stroke-width="2" fill="none"/></svg>Climate Proof</li>
        <li class="feature"><svg class="tick" viewBox="0 0 14 14"><rect width="14" height="14" fill="var(--accent)"/><path d="M3 7l3 3 5-6" stroke="#1a1a1a" stroke-width="2" fill="none"/></svg>Cyclone Rated (Cat. 5)</li>
      </ul>
    </div>
  </section>

  <section class="card card-back" aria-label="Business card back">
    <div class="back-brand">
      <span class="brand-mark"></span>
      <span class="brand-name">Norvale Building Company</span>
    </div>
  </section>

</main>
</body>
</html>
```